Redesign current business card for food company

i would like to redesign my business card. our company is food company, our product range from chips, juices, milk and etc (mostly dried food stuff).
I want o keep same logo but , the rest is open to new design.
you can check at our website about our company www.torvikeats.com

Target Market(s)

most of food company

Industry/Entity Type

Business

Contact Information for Business Card

I want to keep more to blue color...

Colors
3176b5
abd036

Requirements
Must have
• our old logo
Nice to have
• we do not mind to have nice material on bus card in order to accomplish nice design. for example: using spot uv, embossed and etc.

```html
<!DOCTYPE html>
<html lang="en">
<head>
<meta charset="utf-8">
<title>Torvik business card</title>
<link rel="stylesheet" href="https://fonts.googleapis.com/css2?family=Nunito:wght@400;700;800&display=swap">
<style>
  :root {
    --stage: #212121;
    --brand-indigo: #33338f;
    --brand-blue: #2e6fb0;
    --brand-cyan: #15a6cc;
    --brand-green: #abd036;
    --ink: #111111;
    --paper: #ffffff;
  }
  * { margin: 0; padding: 0; box-sizing: border-box; }
  html, body {
    width: 1189px; height: 1200px; overflow: hidden;
    background: var(--stage);
    font-family: "Nunito", Arial, sans-serif;
  }
  .card {
    position: absolute;
    left: 171px;
    width: 856px;
    height: 488px;
    border-radius: 26px;
    overflow: hidden;
    box-shadow: 6px 10px 18px rgba(0,0,0,0.6);
  }
  .card--front {
    top: 68px;
    background:
      radial-gradient(ellipse 60% 70% at 52% 58%, var(--brand-cyan) 0%, var(--brand-blue) 55%, var(--brand-indigo) 100%);
  }
  .card--front .wordmark {
    position: absolute;
    left: 0; right: 0; top: 128px;
    text-align: center;
    font-weight: 800;
    font-size: 150px;
    line-height: 1;
    letter-spacing: -2px;
    color: var(--paper);
  }
  .card--back {
    top: 626px;
    background: var(--paper);
  }
  .back-logo {
    position: absolute;
    left: 36px; top: 146px;
    display: flex; align-items: center; gap: 14px;
  }
  .back-logo .dot {
    width: 26px; height: 26px; border-radius: 50%;
    background: var(--brand-green);
  }
  .back-logo .wordmark {
    font-weight: 800;
    font-size: 96px;
    line-height: 1;
    letter-spacing: -1px;
    color: var(--brand-indigo);
  }
  .divider {
    position: absolute;
    left: 410px; top: 72px;
    width: 2px; height: 268px;
    background: var(--brand-indigo);
  }
  .contact {
    position: absolute;
    left: 439px; top: 78px;
    color: var(--ink);
  }
  .contact .name {
    font-weight: 800;
    font-size: 28px;
    line-height: 32px;
    color: var(--brand-indigo);
  }
  .contact .role {
    font-size: 20px;
    line-height: 22px;
  }
  .contact .address {
    margin-top: 50px;
    font-size: 21px;
    line-height: 29px;
    font-style: normal;
  }
  .contact ul { list-style: none; margin-top: 6px; }
  .contact li {
    display: flex; align-items: center; gap: 10px;
    font-size: 21px; line-height: 27px;
  }
  .contact li svg { width: 19px; height: 17px; fill: var(--brand-indigo); flex: none; }
  .wave { position: absolute; left: 0; bottom: 0; width: 856px; height: 488px; }
  .website {
    position: absolute;
    right: 34px; bottom: 32px;
    font-size: 20px;
    color: var(--paper);
  }
</style>
</head>
<body>

<section class="card card--front">
  <div class="wordmark">torvik</div>
</section>

<section class="card card--back">
  <svg class="wave" viewBox="0 0 856 488" aria-hidden="true">
    <defs>
      <linearGradient id="bandGradient" x1="0" x2="1" y1="0" y2="0">
        <stop offset="0" stop-color="#33338f"/>
        <stop offset="0.5" stop-color="#0faed0"/>
        <stop offset="1" stop-color="#33338f"/>
      </linearGradient>
    </defs>
    <path d="M0 372 C150 430 300 470 420 458 C560 445 700 380 840 370 L856 370 L856 488 L0 488 Z" fill="url(#bandGradient)"/>
    <path d="M0 380 C160 440 300 468 420 456 C560 442 700 378 840 372 L856 372 L856 366 C700 360 560 430 420 448 C300 462 160 430 0 372 Z" fill="#ffffff"/>
    <path d="M4 376 C160 436 300 462 420 448 C560 432 700 362 846 362 C700 350 560 418 420 440 C300 456 160 428 4 376 Z" fill="#000000"/>
  </svg>

  <div class="back-logo">
    <span class="wordmark">torvik</span>
    <span class="dot"></span>
  </div>

  <div class="divider"></div>

  <div class="contact">
    <div class="name">Daniel Hartono</div>
    <div class="role">President</div>
    <address class="address">2418 Orchard Ave<br>Glendale, CA 91204</address>
    <ul>
      <li><svg viewBox="0 0 20 18"><path d="M2 6 C2 2 18 2 18 6 L15 7 L14 5 L6 5 L5 7 Z M5 8 L15 8 L17 16 L3 16 Z"/></svg>555-214-3080</li>
      <li><svg viewBox="0 0 20 18"><path d="M5 1 H15 V6 H5 Z M1 7 H19 V14 H16 V17 H4 V14 H1 Z"/></svg>555-214-3091</li>
      <li><svg viewBox="0 0 20 18"><path d="M6 0 H14 V18 H6 Z M7.5 2 V8 H12.5 V2 Z"/></svg>555 378 6142</li>
      <li><svg viewBox="0 0 20 18"><path d="M1 3 H19 V15 H1 Z M2 4 L10 10 L18 4 V5 L10 11 L2 5 Z" fill-rule="evenodd"/></svg>Daniel@torvikeats.com</li>
    </ul>
  </div>

  <div class="website">www.torvikeats.com</div>
</section>

</body>
</html>
```